Drag Show Flyer

We are holding a Drag Show, we are looking for something fun and exciting, over the top is a must.

Show Date: Saturday September 2nd 2017
Venue: Copper Kettle Cafe Bunbury
Doors open 7pm
Tickets: $50 per person, includes glass of sparkling on arrival and canapes
Tickets available at the Venue or from ticketlorna.com.au

Target Market(s)

Female, Hens Party, LBGT

Industry/Entity Type

Entertainment

Colors

Designer to choose colors to be used in the design.

Requirements
Must have
• Show Date: Saturday September 2nd 2017
• Venue: Copper Kettle Cafe Bunbury
• Doors open 7pm
• Tickets: $50 per person, includes glass of sparkling on arrival and canapes
• Tickets available at the Venue or from ticketlorna.com.au

```html
<!DOCTYPE html>
<html lang="en">
<head>
<meta charset="utf-8">
<title>Drag Show Flyer – Copper Kettle Cafe Bunbury</title>
<link rel="stylesheet" href="https://fonts.googleapis.com/css2?family=Rye&family=Oswald:wght@500;600&display=swap">
<style>
  :root {
    --stage: #c9cacb;
    --magenta: #9c1f6a;
    --magenta-shadow: #4a0c30;
    --gold-top: #ffe35a;
    --gold-bottom: #f6b21a;
    --ink: #1b1408;
    --white: #ffffff;
    --night: #050505;
    --orange: #f06a1a;
    --amber: #f3a21c;
    --lime: #7fc23a;
    --green: #2f8f3a;
    --teal: #2ea7a3;
  }
  * { margin: 0; padding: 0; box-sizing: border-box; }
  html, body { width: 1200px; height: 801px; overflow: hidden; }
  body { background: var(--stage); position: relative; }

  .flyer {
    position: absolute; left: 336px; top: 28px;
    width: 527px; height: 745px; overflow: hidden;
    background: var(--night);
  }
  .flyer__backdrop {
    position: absolute; inset: 0;
    background:
      radial-gradient(ellipse 60% 40% at 55% 58%, rgba(140,220,90,.55), rgba(0,0,0,0) 70%),
      linear-gradient(180deg, rgba(0,0,0,0) 0%, rgba(0,0,0,0) 48%, rgba(5,5,5,.85) 66%, var(--night) 78%),
      linear-gradient(160deg, var(--green) 0%, var(--lime) 28%, var(--amber) 55%, var(--orange) 80%, #d8321b 100%);
  }

  .title {
    position: absolute; left: 48px; top: 62px; width: 460px; height: 140px;
    font-family: "Rye", serif; color: var(--magenta);
    text-shadow: 3px 4px 4px var(--magenta-shadow);
  }
  .title__initial { position: absolute; left: 0; top: 0; font-size: 122px; line-height: 1; }
  .title__line { position: absolute; left: 88px; font-size: 46px; line-height: 1; white-space: nowrap; }
  .title__line--top { top: 14px; }
  .title__line--bottom { top: 74px; }

  .date-band {
    position: absolute; left: 41px; top: 209px; width: 459px; height: 51px;
    border-radius: 10px;
    background: linear-gradient(180deg, var(--gold-top), var(--gold-bottom));
    box-shadow: 0 2px 6px rgba(0,0,0,.35);
    display: flex; align-items: center; justify-content: center;
    font-family: "Oswald", sans-serif; font-weight: 600; font-size: 27px;
    letter-spacing: 1px; color: var(--ink);
  }

  .tickets {
    position: absolute; left: 0; width: 527px; text-align: center;
    font-family: "Rye", serif; color: var(--white); white-space: nowrap;
    text-shadow: 2px 2px 3px rgba(0,0,0,.7);
  }
  .tickets__price { top: 266px; font-size: 23px; line-height: 34px; }
  .tickets__extras { top: 304px; font-size: 15px; line-height: 25px; }

  .sponsor {
    position: absolute; left: 37px; width: 121px; height: 68px;
    display: flex; align-items: center; justify-content: center;
    font-family: "Oswald", sans-serif; font-weight: 500; font-size: 13px;
    text-align: center; line-height: 1.1; padding: 4px;
  }
  .sponsor--host { top: 458px; background: #0c0c0c; color: var(--white); }
  .sponsor--producer { top: 534px; background: #f3f3f3; color: var(--magenta); }
  .sponsor--partner { top: 610px; background: var(--white); color: var(--teal); }

  .details {
    position: absolute; left: 230px; width: 230px; text-align: center;
    font-family: "Oswald", sans-serif; color: var(--white); white-space: nowrap;
  }
  .details__label { top: 527px; font-size: 15px; font-weight: 500; }
  .details__time { top: 541px; font-size: 32px; font-weight: 600; }
  .details__rule { position: absolute; left: 258px; top: 601px; width: 170px; height: 1px; background: rgba(255,255,255,.6); }
  .details__where { left: 193px; width: 304px; top: 611px; font-size: 13.5px; font-weight: 500; letter-spacing: .5px; }
  .details__url { left: 193px; width: 304px; top: 626px; font-size: 31px; font-weight: 600; }
</style>
</head>
<body>
  <main class="flyer">
    <div class="flyer__backdrop" role="img" aria-label="Glowing orange-to-green halftone dot backdrop with a cheering crowd silhouette fading into black"></div>

    <h1 class="title">
      <span class="title__initial">C</span>
      <span class="title__line title__line--top">OPPER KETTLE</span>
      <span class="title__line title__line--bottom">CAFE BUNBURY</span>
    </h1>

    <p class="date-band">SATURDAY SEPTEMBER 2ND 2017</p>

    <p class="tickets tickets__price">TICKETS: $50 PER PERSON,</p>
    <p class="tickets tickets__extras">INCLUDES GLASS OF SPARKLING ON<br>ARRIVAL AND CANAPES</p>

    <div class="sponsor sponsor--host">Copper Kettle Cafe</div>
    <div class="sponsor sponsor--producer">Loud Lips Productions</div>
    <div class="sponsor sponsor--partner">Velvet Circle Group</div>

    <p class="details details__label">DOORS OPEN</p>
    <p class="details details__time">07:00 PM</p>
    <div class="details__rule"></div>
    <p class="details details__where">TICKETS AVAILABLE AT THE VENUE OR FROM</p>
    <p class="details details__url">TICKETLORNA.COM.AU</p>
  </main>
</body>
</html>
```